Gerald Munro - Corporate MC & Entertainer

Design a one page A4 flyer
I'm after a one Page Flyer
A4 Size - One sided
I want the finished artwork in 2 Forms.
1/ One that I could print out myself in a small run ( I have a Vextra Colour PrintJet)
or send out as a PDF
2/ A second version that could be printed commercially , so including bleed crop marks so it can be cut to A4 size
I have attached the copy that should be included. (Podium Pulse 2014 WORDS)
If there was too much text to include , we could drop one of the testimonial quotes
I have attached 3 images that could be included if there is room.
If there were too many images I suggest dropping Image 3 ( with bow tie)
As you can see from the copy (or a visit to my website) there are two main services that I provide
Corporate MC Services and Entertainment Services.
These are however intertwined - My MC work often includes some entertaining effects from my ThoughtCatcher Act. I often get booked to MC a conference and provide a show.
I'm after something that is -
Classy , Sophisticated, Smart, perhaps a bit quirky.
Nothing "Magic" like - eg no Rabbits , Wands, puffs of smoke
I have no corporate colour or logo or branding that should be included
You can see some previous flyers here http://www.proflinknet.com/in/geraldmunro
I like these, but looking for new ideas
Target Market(s)
Corporate , Conference Organisers, Speaker Bureau owners, Large Association Conference committees
Industry/Entity Type
Entertainment
Colors
Designer to choose colors to be used in the design.
Look and feel

```html
<!DOCTYPE html>
<html lang="en">
<head>
<meta charset="utf-8">
<title>Gerald Munro – Corporate MC &amp; Entertainer</title>
<link href="https://fonts.googleapis.com/css2?family=Archivo+Black&family=Bebas+Neue&family=Open+Sans:ital,wght@0,400;0,700;1,400&display=swap" rel="stylesheet">
<style>
  :root{
    --stage:#6d6e71;
    --green:#8cc43f;
    --charcoal:#3a3a3c;
    --blue:#29abe2;
    --night:#0b0b0d;
    --ink:#1e1e1e;
    --white:#ffffff;
  }
  *{margin:0;padding:0;box-sizing:border-box}
  html,body{width:1200px;height:999px;overflow:hidden;background:var(--stage)}
  .flyer{position:absolute;left:315px;top:40px;width:612px;height:925px;background:var(--green);font-family:"Open Sans",sans-serif}
  .side{position:absolute;left:0;top:0;width:203px;height:925px;background:var(--charcoal)}
  .tagline{position:absolute;left:0;top:80px;width:203px;text-align:center;color:var(--white)}
  .tagline .country{font-family:"Bebas Neue",sans-serif;font-size:42px;line-height:38px;display:block}
  .tagline .role{font-family:"Bebas Neue",sans-serif;font-size:31px;line-height:30px;display:block}
  .tagline .mind{font-family:"Archivo Black",sans-serif;font-size:38px;line-height:40px;display:block;transform:scaleX(1.3)}
  .services{position:absolute;left:0;top:232px;width:203px;text-align:center;color:var(--white);font-weight:700;font-size:24px;line-height:33px}
  .stage-photo{position:absolute;left:0;top:315px;width:203px;height:295px;background:radial-gradient(circle at 45% 55%,#2c3a78 0,#101224 45%,var(--night) 80%)}
  .testimonials{position:absolute;left:10px;top:622px;width:176px;color:var(--white)}
  .testimonials h2{font-family:"Bebas Neue",sans-serif;font-weight:400;font-size:25px;line-height:30px;margin-bottom:10px}
  .quote{font-style:italic;font-size:11px;line-height:16px;text-align:justify}
  .source{font-size:11px;line-height:16px;margin:16px 0 22px}
  .name{position:absolute;left:203px;top:8px;width:409px;text-align:center;font-family:"Bebas Neue",sans-serif;font-size:76px;line-height:80px;color:var(--white)}
  .hero-photo{position:absolute;left:203px;top:88px;width:409px;height:324px;background:radial-gradient(circle at 60% 45%,#3a3a3e 0,#141416 45%,var(--night) 75%)}
  .headline{position:absolute;left:203px;top:412px;width:409px;height:98px;background:var(--blue);color:var(--white);text-align:center}
  .headline .top{display:block;font-family:"Bebas Neue",sans-serif;font-size:44px;line-height:44px;padding-top:10px}
  .headline .big{display:block;font-family:"Archivo Black",sans-serif;font-size:36px;line-height:38px;transform:scaleX(1.35)}
  .bio{position:absolute;left:213px;top:522px;width:388px;font-size:11.4px;line-height:16px;color:var(--ink);text-align:justify}
  .bio p{margin-bottom:16px}
  .upcoming{position:absolute;left:208px;top:738px;width:240px;text-align:center;color:var(--ink)}
  .upcoming .ask{display:block;font-family:"Bebas Neue",sans-serif;font-size:34px;line-height:36px}
  .upcoming .year{display:block;font-family:"Bebas Neue",sans-serif;font-size:74px;line-height:70px;color:var(--white)}
  .upcoming .cta{display:block;font-weight:700;font-size:18px;line-height:25px;margin-top:6px}
  .portrait{position:absolute;left:464px;top:730px;width:131px;height:180px;background:linear-gradient(180deg,#f2f2f2 0,#d8d8d8 45%,#1c1c1c 46%,#0e0e0e 100%)}
</style>
</head>
<body>
  <main class="flyer">
    <aside class="side">
      <h2 class="tagline">
        <span class="country">Australia's</span>
        <span class="role">Magician of the</span>
        <span class="mind">MIND</span>
      </h2>
      <p class="services">Corporate MC<br>&amp; Entertainer</p>
      <div class="stage-photo" role="img" aria-label="Gerald Munro on stage with arms outstretched under starry lights"></div>
      <section class="testimonials">
        <h2>Recent Testimonials</h2>
        <p class="quote">"A big thank you for a really good job on Friday night which was carried out with aplomb - well done!"</p>
        <p class="source">- Growers &amp; Garden Guild</p>
        <p class="quote">"Huge thanks for your professionalism with the Awards, getting a laugh from everyone and in general creating an atmosphere that was enjoyable and relaxed!"</p>
        <p class="source">- HomeTend</p>
      </section>
    </aside>

    <h1 class="name">Gerald Munro</h1>
    <div class="hero-photo" role="img" aria-label="Gerald Munro smiling and pointing, in a dark suit against a starry backdrop"></div>
    <h2 class="headline"><span class="top">Solving your conference</span><span class="big">PUZZLES!</span></h2>

    <section class="bio">
      <p>In the last two years Gerald has been engaged as the Conference MC for events in Hawaii, New Zealand, Hong Kong &amp; all States of Australia.</p>
      <p>He facilitated 24 Australian Major Project Conferences for ForumWorks and 16 International CEO Summits for Apex Summit Group.</p>
      <p>In the Australian Corporate Sector, he managed major events for - BrokerNet Oz, IBCA, HomeTend, Signal Hire, Parish Care and the Growers &amp; Garden Guild.</p>
      <p>As an Entertainer he cruised the world on several luxury cruise ships, visiting Japan, Korea, China, Tahiti and New Zealand in his travels.</p>
    </section>

    <section class="upcoming">
      <span class="ask">What's coming up in</span>
      <span class="year">2014?</span>
      <span class="cta">Get involved at<br>www.GeraldMunro.com</span>
    </section>
    <div class="portrait" role="img" aria-label="Gerald Munro in a tuxedo and bow tie with glasses"></div>
  </main>
</body>
</html>
```